NZ's Most interesting purveyor of industrial furniture & exotic taxidermy needs a creative generic s

BRUX Heritage is seller of rustic industrial furniture, accessories, cowhides, antler chandeliers and taxidermy with two stores in Auckland, Ponsonby and Mt Eden. We need a luggage style swingtag which we would like to have on every piece of furniture and large item to add to the story of our brand. These tags will be generic and will not have any individual item information on them. The tags are to include the logo, our website and a small story about our brand. The inside card showing photo scenes of our industrial eclectic style. Specs and sizing of tag as attached. The overall design should exude an authentic, industrial vintage vibe.

Reason: Only two designs have been submitted.

Industry/Entity Type

Industrial

Requirements
Must have
• logo , images, website. Must have the insert card and layout as attached.

```html
<!DOCTYPE html>
<html lang="en">
<head>
<meta charset="utf-8">
<title>BRUX Heritage – Swing Tag Set</title>
<link rel="stylesheet" href="https://fonts.googleapis.com/css2?family=Tinos:ital,wght@0,400;0,700;1,700&display=swap">
<style>
  :root {
    --backdrop: #ececec;
    --kraft: #8c7452;
    --kraft-shade: #7f684a;
    --ink: #3b2f22;
    --photo-light: #c9c4ba;
    --photo-dark: #4a4039;
  }
  * { box-sizing: border-box; margin: 0; padding: 0; }
  html, body { width: 1200px; height: 1200px; overflow: hidden; }
  body {
    position: relative;
    background: var(--backdrop);
    font-family: "Tinos", "Times New Roman", serif;
    color: var(--ink);
  }
  .card {
    position: absolute;
    background: var(--kraft);
    box-shadow: 0 2px 6px rgba(0,0,0,0.18);
  }

  /* Tall swing tag */
  .tag-front {
    left: 70px; top: 90px; width: 330px; height: 640px;
    display: flex; flex-direction: column; align-items: center;
    padding: 50px 30px 40px;
  }
  .icon-column {
    width: 150px; height: 380px;
    background: linear-gradient(180deg, var(--kraft-shade), #6e5a40);
    border-radius: 6px;
  }
  .brand-name {
    margin-top: 48px;
    text-align: center;
    font-weight: 700;
    line-height: 1;
  }
  .brand-name .line-1 { display: block; font-size: 52px; letter-spacing: 4px; }
  .brand-name .line-2 { display: block; font-size: 48px; margin-top: 4px; }
  .site-url { margin-top: 6px; font-size: 15px; font-weight: 700; letter-spacing: 0.5px; }

  /* Insert card with photo */
  .insert-card {
    left: 450px; top: 300px; width: 690px; height: 300px;
    display: flex; align-items: center;
  }
  .insert-copy {
    width: 290px; text-align: center; padding-left: 20px;
  }
  .insert-copy .brand-name { margin-top: 0; }
  .insert-copy .line-1 { font-size: 40px; letter-spacing: 3px; }
  .insert-copy .line-2 { font-size: 36px; }
  .insert-copy .site-url { font-size: 13px; }
  .offer-list {
    margin-top: 16px; list-style: none; font-size: 15px; font-weight: 700; line-height: 1.45;
  }
  .insert-photo {
    width: 300px; height: 260px; margin-left: 20px;
    background: linear-gradient(160deg, var(--photo-light) 0%, #8f877c 55%, var(--photo-dark) 100%);
  }

  /* Story card */
  .story-card {
    left: 110px; top: 800px; width: 720px; height: 300px;
    padding: 18px;
  }
  .story-frame {
    width: 100%; height: 100%;
    border: 2px solid var(--ink);
    text-align: center;
    padding: 26px 40px;
  }
  .story-title { font-size: 28px; font-weight: 700; margin-bottom: 14px; }
  .story-text { font-size: 18px; font-weight: 700; font-style: italic; line-height: 1.45; text-align: justify; text-align-last: center; }
</style>
</head>
<body>

  <section class="card tag-front">
    <div class="icon-column" role="img" aria-label="Stacked icons of an antelope head, sofa, chandelier and bead necklace"></div>
    <h1 class="brand-name"><span class="line-1">BRUX</span><span class="line-2">Heritage</span></h1>
    <p class="site-url">BRUXHERITAGE.COM</p>
  </section>

  <section class="card insert-card">
    <div class="insert-copy">
      <h2 class="brand-name"><span class="line-1">BRUX</span><span class="line-2">Heritage</span></h2>
      <p class="site-url">BRUXHERITAGE.COM</p>
      <ul class="offer-list">
        <li>Furniture • Accessories</li>
        <li>Taxedermy • Cowhides</li>
        <li>Chandeliers • Antlers</li>
      </ul>
    </div>
    <div class="insert-photo" role="img" aria-label="Showroom photo with leather armchairs, mounted horse head, cowhide rug and industrial tables"></div>
  </section>

  <section class="card story-card">
    <div class="story-frame">
      <h2 class="story-title">Our Goals</h2>
      <p class="story-text">Sed tristique aliquam metus, nec eleifend metus tincidunt quis. Morbi est magna, elementum vitae erat id, lacinia pretium nunc. Nunc mollis ante ac accumsan bibendum. Maecenas ac varius orci. Cras non turpis in mauris euismod ultricies placerat id lectus. Aliquam nec porttitor ipsum</p>
    </div>
  </section>

</body>
</html>
```